Business Card Design for Clinical Therapist

I will operate in 3 product areas as follows...
I will operate as Psychotherapist providing an opportunity for individuals to stop, reflect, heal, and gain hope in a safe and professional atmosphere. My task as a Licensed Mental Health Social Worker is to work “along-side” the client to help guide them toward answers they may seek. I believe that all difficulties contain a small seed of opportunity within them and I can support the individual in clarifying issues while resolving obstacles that may get in the way.
1-Therapy
Treatment Issues may include:
• Addiction
• Bipolar Disorder
• Adolescent or Adult
• Coping Skills
• Dual Diagnosis
• Family Conflict
• Sleep or Insomnia
• Substance Abuse
• Anger Management
• Career Counseling
• Drug Abuse
• Emotional Disturbance
• Grief
• Self Esteem
• Trauma and PTSD
Treatment Orientation may include but not be limited to:
• CBT
• EMDR
• Person-Centered
• Mindfulness based (MBCT)
• Motivational Interviewing

2-Other Substance Abuse Services
SAP Assessments
Employees performing safety-sensitive duties under US Bureau of Roadway Affairs rules must have an evaluation by a qualified Substance Abuse Professional when they are in violation of BRA rules (for a positive test or a refusal to test). I am a BRA qualified SAP and can perform these evaluations, which involve specialized assessment and compliance reports, as well as a return to work assessment.

3-DUI/OVUII Assessments
Substance abuse assessment reports-State level assessments targeted for the court system.

Somehow I would like the final design to acknowledge the three areas of services, or two being therapy for mental health services and combining SAP/OVUII assessment reporting for Substance abuse)

Industry/Entity Type

Mental Health

Contact Information for Business Card

Brightwell Harbor LLC,
Desmond Farrowby LCSW
Clinical Therapist
2087 West Palmer Avenue, STE 412
Honolulu, HI 96720
808.555.0193
brightwellharborllc.example

Colors

Designer to choose colors to be used in the design.

```html
<!DOCTYPE html>
<html lang="en">
<head>
<meta charset="utf-8">
<title>Brightwell Harbor LLC — Business Card</title>
<link rel="stylesheet" href="https://fonts.googleapis.com/css2?family=Didact+Gothic&display=swap">
<style>
  :root {
    --teal: #25bfb1;
    --charcoal: #474747;
    --orange: #f2982c;
    --white: #ffffff;
    --ink-soft: #e9e9e9;
    --backdrop: #eceae6;
    --teal-deep: #1d8f85;
  }
  * { box-sizing: border-box; margin: 0; padding: 0; }
  html, body { width: 1200px; height: 873px; overflow: hidden; }
  body {
    background: var(--backdrop);
    font-family: "Didact Gothic", sans-serif;
    position: relative;
  }
  .card {
    position: absolute;
    left: 260px;
    width: 680px;
    height: 388px;
    border-radius: 34px;
    overflow: hidden;
    box-shadow: 0 6px 18px rgba(0,0,0,0.18);
  }
  /* Front */
  .card-front { top: 30px; background: var(--teal); }
  .front-header {
    position: absolute; left: 0; top: 0; width: 100%; height: 118px;
    background: var(--charcoal);
  }
  .front-footer {
    position: absolute; left: 0; bottom: 0; width: 100%; height: 44px;
    background: var(--charcoal);
  }
  .brand {
    position: absolute; left: 40px; top: 44px;
    display: flex; align-items: center; gap: 16px;
  }
  .brand-dot {
    width: 64px; height: 64px; border-radius: 50%;
    background: var(--orange);
  }
  .brand-name {
    color: var(--teal);
    font-size: 34px;
    letter-spacing: 1px;
    text-transform: uppercase;
  }
  .identity {
    position: absolute; right: 46px; top: 128px; text-align: right;
  }
  .person-name { color: var(--white); font-size: 30px; letter-spacing: 0.5px; }
  .person-title { color: var(--teal-deep); font-size: 20px; margin-top: 2px; }
  .contact {
    position: absolute; left: 44px; top: 222px;
    list-style: none; color: var(--white); font-size: 19px; line-height: 27px;
  }
  .contact li { display: flex; align-items: flex-start; gap: 12px; }
  .contact svg { width: 15px; height: 15px; margin-top: 6px; flex: none; }
  .contact .indent { padding-left: 27px; }

  /* Back */
  .card-back { top: 448px; background: var(--charcoal); }
  .back-services {
    position: absolute; left: 30px; top: 30px;
    display: flex; gap: 34px; color: var(--ink-soft);
    font-size: 13px; line-height: 18px;
  }
  .service-heading { font-size: 16px; color: var(--white); }
  .service-list { list-style: none; padding-left: 12px; }
  .service-list li::before { content: "• "; }
  .back-panel {
    position: absolute; right: 0; top: 0; width: 252px; height: 100%;
    background: var(--teal); padding: 28px 22px 0 20px;
    color: var(--charcoal); font-size: 11.5px; line-height: 15px;
  }
  .panel-heading { font-size: 13px; margin-bottom: 4px; }
  .panel-block { margin-bottom: 14px; }
  .back-brand {
    position: absolute; left: 20px; bottom: 30px;
    display: flex; align-items: center; gap: 8px;
  }
  .back-brand .brand-dot { width: 26px; height: 26px; }
  .back-brand .brand-name { color: var(--charcoal); font-size: 15px; letter-spacing: 0.5px; }
</style>
</head>
<body>

<section class="card card-front" aria-label="Business card front">
  <div class="front-header"></div>
  <div class="front-footer"></div>
  <div class="brand">
    <span class="brand-dot"></span>
    <span class="brand-name">Brightwell Harbor LLC</span>
  </div>
  <div class="identity">
    <p class="person-name">Desmond Farrowby, LCSW</p>
    <p class="person-title">Clinical Therapist</p>
  </div>
  <ul class="contact">
    <li>
      <svg viewBox="0 0 16 16" aria-hidden="true"><path fill="#333" d="M3 2h3l1.5 3.5-2 1.2a9 9 0 0 0 3.8 3.8l1.2-2L14 10v3c0 .6-.4 1-1 1A11 11 0 0 1 2 3c0-.6.4-1 1-1z"/></svg>
      <span>808.555.0193</span>
    </li>
    <li>
      <svg viewBox="0 0 16 16" aria-hidden="true"><circle cx="8" cy="8" r="6.5" fill="none" stroke="#333" stroke-width="1.6"/><path d="M1.5 8h13M8 1.5c-3 3.5-3 9.5 0 13M8 1.5c3 3.5 3 9.5 0 13" fill="none" stroke="#333" stroke-width="1.2"/></svg>
      <span>brightwellharborllc.example</span>
    </li>
    <li>
      <svg viewBox="0 0 16 16" aria-hidden="true"><path fill="#333" d="M8 1.5 1 8h2v6.5h4V10h2v4.5h4V8h2z"/></svg>
      <span>2087 West Palmer Avenue,</span>
    </li>
    <li class="indent">STE 412 Honolulu, HI 96720</li>
  </ul>
</section>

<section class="card card-back" aria-label="Business card back">
  <div class="back-services">
    <div class="service-column">
      <p class="service-heading">Therapy</p>
      <p>Treatment Issues<br>will include</p>
      <ul class="service-list">
        <li>Addiction</li>
        <li>Bipolar Disorder</li>
        <li>Child or Adolescent</li>
        <li>Coping Skills</li>
        <li>Dual Diagnosis</li>
        <li>Family Conflict</li>
        <li>Sleep or Insomnia</li>
        <li>Substance Abuse</li>
        <li>Anger Management</li>
        <li>Career Counseling</li>
        <li>Drug Abuse</li>
        <li>Emotional Disturbance</li>
        <li>Grief</li>
        <li>Self Esteem</li>
        <li>Trauma and PTSD</li>
      </ul>
    </div>
    <div class="service-column">
      <p class="service-heading">&nbsp;</p>
      <p>Treatment Orientation<br>will include<br>but not be limited to:</p>
      <ul class="service-list">
        <li>CBT</li>
        <li>EMDR</li>
        <li>Person-Centered</li>
        <li>Mindfulness based (MBCT)</li>
        <li>Motivational Interviewing</li>
      </ul>
    </div>
  </div>
  <div class="back-panel">
    <div class="panel-block">
      <p class="panel-heading">Other Substance Abuse Professional Services</p>
      <p>• SAP Services: Employees performing safety-sensitive duties under US Bureau of Roadway Affairs rules must have an evaluation by a qualified Substance Abuse Professional when they are in violation of BRA rules (for a positive test or a refusal to test).</p>
    </div>
    <div class="panel-block">
      <p class="panel-heading">DUI/OVUII:</p>
      <p>• Substance abuse assessment reports<br>• State level assessments targeted for the court system</p>
    </div>
    <div class="back-brand">
      <span class="brand-dot"></span>
      <span class="brand-name">BRIGHTWELL HARBOR LLC</span>
    </div>
  </div>
</section>

</body>
</html>
```